Tallow Creek Partners needs an email sign off and professional power point template

Newly formed company and we require:1. graphic email signature on our email , and2.a professional powerpoint template (title page and sub pages) and revamp of the attached powerpoint presentation I have uploaded our business car design (logo and contact details ) and a current powerpoint template we are currently working with. Also a brief of how we operateOur mantra is Discover, Develop, Deliver.

Target Market(s)

multinationals and mid size SME's requiring help to grown new markets or geographies for their business.

Colors
000000

Requirements
Must have
• the mantra..our phases of engagement around assisting clients is:
• 1. Discover
• 2. Develop
• 3. Deliver
Nice to have
• we differentiate ourselves form consultant by actually executing the plan for them (i.e. is the delivery phase)

```html
<!DOCTYPE html>
<html lang="en">
<head>
<meta charset="utf-8">
<title>Tallow Creek Partners — Title Slide</title>
<link href="https://fonts.googleapis.com/css2?family=Oswald:wght@500;700&display=swap" rel="stylesheet">
<style>
  :root {
    --navy: #041a33;
    --teal: #025874;
    --band-light: #ffffff;
    --band-mid: #f2f2f2;
    --band-edge: #e2e2e2;
    --silver: #9a9a9a;
    --silver-dark: #5a5a5a;
    --white: #ffffff;
  }
  html, body {
    margin: 0;
    padding: 0;
    width: 1200px;
    height: 1000px;
    overflow: hidden;
    background: var(--white);
  }
  .slide {
    position: relative;
    width: 1200px;
    height: 1000px;
    overflow: hidden;
    font-family: "Oswald", "Arial Narrow", sans-serif;
  }
  .top-band {
    position: absolute;
    left: 0; top: 0;
    width: 1200px; height: 272px;
    background: var(--navy);
  }
  .light-band {
    position: absolute;
    left: 0; top: 272px;
    width: 1200px; height: 320px;
    background: radial-gradient(ellipse at 35% 50%, var(--band-light) 0%, var(--band-mid) 60%, var(--band-edge) 100%);
  }
  .bottom-band {
    position: absolute;
    left: 0; top: 592px;
    width: 1200px; height: 408px;
    background: var(--teal);
  }
  .band-edges {
    position: absolute;
    left: 0; top: 250px;
    width: 1200px; height: 360px;
  }
  .brand {
    position: absolute;
    left: 0; top: 272px;
    width: 1200px; height: 320px;
    display: flex;
    align-items: center;
    justify-content: center;
    gap: 18px;
  }
  .brand-mark {
    width: 40px; height: 40px;
    background: var(--teal);
  }
  .brand-name {
    font-weight: 700;
    font-size: 72px;
    letter-spacing: 1px;
    color: var(--navy);
    text-transform: uppercase;
    line-height: 1;
  }
  .headline {
    position: absolute;
    left: 0; top: 672px;
    width: 1200px;
    margin: 0;
    text-align: center;
    font-weight: 700;
    font-size: 68px;
    line-height: 1;
    color: var(--white);
    text-transform: uppercase;
    letter-spacing: 0.5px;
  }
  .mantra {
    position: absolute;
    left: 0; top: 760px;
    width: 1200px;
    margin: 0;
    padding: 0;
    list-style: none;
    display: flex;
    justify-content: center;
    font-weight: 700;
    font-size: 27px;
    line-height: 1.2;
    color: var(--white);
    text-transform: uppercase;
  }
  .mantra li {
    padding: 0 9px;
  }
  .mantra li + li {
    border-left: 1px solid var(--white);
  }
</style>
</head>
<body>
  <main class="slide">
    <div class="top-band"></div>
    <div class="light-band"></div>
    <div class="bottom-band"></div>

    <svg class="band-edges" viewBox="0 250 1200 360" width="1200" height="360" aria-hidden="true">
      <defs>
        <linearGradient id="edge-top" x1="0" y1="0" x2="1" y2="0">
          <stop offset="0" stop-color="#ffffff" stop-opacity="0"/>
          <stop offset="0.35" stop-color="#d8d8d8"/>
          <stop offset="0.7" stop-color="#8a8a8a"/>
          <stop offset="1" stop-color="#3a3a3a" stop-opacity="0.6"/>
        </linearGradient>
        <linearGradient id="edge-bottom" x1="0" y1="0" x2="1" y2="0">
          <stop offset="0" stop-color="#ffffff" stop-opacity="0"/>
          <stop offset="0.3" stop-color="#e0e0e0"/>
          <stop offset="0.7" stop-color="#8a8a8a"/>
          <stop offset="1" stop-color="#2a2a2a" stop-opacity="0.7"/>
        </linearGradient>
      </defs>
      <path d="M0 272 Q600 252 1200 272 L1200 274 Q600 266 0 274 Z" fill="url(#edge-top)"/>
      <path d="M0 584 Q600 594 1200 584 L1200 592 Q600 606 0 592 Z" fill="url(#edge-bottom)"/>
    </svg>

    <div class="brand">
      <span class="brand-mark"></span>
      <span class="brand-name">Tallow Creek</span>
    </div>

    <h1 class="headline">Tallow Creek Partners</h1>
    <ul class="mantra">
      <li>Discover</li>
      <li>Develop</li>
      <li>Deliver</li>
    </ul>
  </main>
</body>
</html>
```